Design Workout/Fitness Mobile App

Create a design for a mobile workout out a mobile app called Brisko Routine. This workout app is very similar to Tandem Sweat Session. Please download or search for the Tandem Sweat Session in the Grove Market to get an idea, I will also include a link below.

App Description: http://lnkwrap.example/q7Rt2Lm

The main difference between Brisko Routine and Tandem Sweat Session is that Brisko Routines are 8 Minutes instead of 7 Minute and Brisko Routine are created/demonstrated by a real human being instead of an animated video.
Please read the referenced Quillbox Doc and install or go through the Tandem Sweat app. I am open to any design color. The app is targetted at people who need a quick workout but do not have a lot of time

Example (Tandem Sweat Session): http://lnkwrap.example/Vx9kPe4

Target Market(s)

Busy working adults

Industry/Entity Type

Fitness

Colors

Designer to choose colors to be used in the design.

Requirements
Must have
• This design is for at least three screens
• The main screen showing a list of the types of exercises such as lower body, abs, etc
• The workout screen showing the video
• A calendar showing the number of days user worked.
Nice to have
• Make the designs close to the Tandem-sweat session with different look and feel

```html
<!DOCTYPE html>
<html lang="en">
<head>
<meta charset="utf-8">
<title>Brisko Routine – App Screens</title>
<link href="https://fonts.googleapis.com/css2?family=Roboto:wght@300;400;500;700&family=Roboto+Condensed:wght@500&display=swap" rel="stylesheet">
<style>
  :root{
    --bg:#8c8b94;
    --blue-deep:#3d5f9e;
    --blue-mid:#3574ad;
    --blue-light:#2c9bd2;
    --accent:#29a8e6;
    --ink:#1f2326;
    --ink-soft:#6b7075;
    --line:#e3e5e8;
    --white:#ffffff;
    --nav-ink:#8a8f94;
  }
  *{box-sizing:border-box;margin:0;padding:0}
  html,body{width:1200px;height:1200px;overflow:hidden;background:var(--bg);font-family:"Roboto",Arial,sans-serif}
  .canvas{position:relative;width:1200px;height:1200px}
  .screen{position:absolute;overflow:hidden;background:var(--white);border-radius:30px}
  .abs{position:absolute}

  /* splash */
  .splash{left:462px;top:-30px;width:280px;height:406px;background:linear-gradient(180deg,var(--blue-deep),var(--blue-light))}
  .brand{font-weight:700;color:var(--white);white-space:nowrap}
  .splash .brand{left:0;width:100%;text-align:center;top:154px;font-size:26px;line-height:32px}
  .btn-outline{left:60px;width:160px;height:33px;border:1.5px solid var(--white);border-radius:17px;color:var(--white);font-size:13.5px;display:flex;align-items:center;justify-content:center}

  .phone{top:530px;width:282px;height:608px}
  .status{top:14px;left:26px;right:22px;height:14px;display:flex;justify-content:space-between;color:var(--white);font-size:10.5px}
  .status svg{height:9px}

  /* home list */
  .home{left:60px}
  .home-header{left:0;top:0;width:100%;height:82px;background:linear-gradient(90deg,var(--blue-mid),#4a5aa0)}
  .home .brand{left:79px;top:47px;font-size:18px;line-height:22px}
  .burger{left:12px;top:49px;width:24px}
  .tabs{left:0;width:100%;height:30px;display:flex;font-size:9.5px;font-weight:500}
  .tab{flex:1;display:flex;align-items:center;justify-content:center;color:var(--ink-soft);border-bottom:2px solid var(--line)}
  .tab.active{color:var(--ink);border-bottom-color:var(--accent)}
  .card{left:0;width:100%;height:119px}
  .card-caption{position:absolute;left:11px;bottom:8px;color:var(--white);font-weight:700;font-size:13px}
  .photo-gym{background:linear-gradient(160deg,#7a8790,#3e4a52 60%,#5f6a70)}
  .photo-push{background:linear-gradient(160deg,#c9c6c1,#8d7a66 55%,#4d4a48)}
  .photo-ball{background:linear-gradient(160deg,#e5e3e0,#b8b6b8 50%,#8f96a6)}

  .navbar{left:0;bottom:0;width:100%;height:50px;background:var(--white);display:flex;justify-content:space-around;align-items:center;padding-top:2px}
  .nav-item{display:flex;flex-direction:column;align-items:center;font-size:7.5px;color:var(--nav-ink);gap:3px;width:60px}
  .nav-item svg{width:20px;height:20px;stroke:var(--nav-ink);fill:none;stroke-width:1.3}
  .nav-item.active{color:var(--accent)}
  .nav-item.active svg{stroke:var(--accent)}

  /* workout detail */
  .detail{left:433px}
  .video{left:0;top:0;width:100%;height:186px}
  .progress{left:6px;right:6px;top:173px;display:flex;align-items:center;gap:6px;color:var(--white);font-size:7.5px}
  .progress .track{flex:1;height:1px;background:rgba(255,255,255,.7);position:relative}
  .progress .knob{position:absolute;left:21%;top:-3px;width:7px;height:7px;border-radius:50%;background:var(--white)}
  .label-small{left:11px;top:201px;font-size:9px;color:var(--ink-soft)}
  .detail-title{left:11px;top:216px;font-size:14px;font-weight:500;color:var(--ink)}
  .detail-desc{left:11px;width:256px;top:238px;font-size:8.1px;line-height:15px;color:#3a3f44}
  .detail .tabs{top:296px;font-weight:400;font-size:9.5px}
  .comment{left:11px;right:9px;display:flex;gap:10px}
  .avatar{width:28px;height:28px;border-radius:50%;background:#dcdde0;border:1px solid #c3c5c9;flex:none}
  .comment-name{font-size:9px;font-weight:500;color:var(--ink)}
  .comment-text{font-size:8.5px;line-height:16px;color:var(--ink-soft);margin-top:3px}
  .comment-meta{font-size:9px;color:var(--ink);margin-top:8px;display:flex;gap:16px;align-items:center}
  .comment-meta span{display:flex;gap:4px;align-items:center}
  .comment-divider{left:11px;right:9px;height:1px;background:var(--line)}
  .comment-input{left:11px;right:9px;top:517px;height:36px;background:#f3f4f5;border:1px solid var(--line);font-size:8.5px;color:#b7bbbf;display:flex;align-items:center;justify-content:space-between;padding:0 12px 0 16px}

  /* steps */
  .steps{left:812px;background:linear-gradient(180deg,#3f5c9c 0%,var(--blue-mid) 45%,var(--blue-light) 100%)}
  .ring{left:36px;top:168px;width:212px;height:212px}
  .step-count{left:0;width:100%;text-align:center;top:282px;font-family:"Roboto Condensed",sans-serif;font-weight:500;font-size:50px;line-height:54px;color:var(--white);letter-spacing:1px}
  .step-label{left:0;width:100%;text-align:center;top:337px;font-size:14px;color:var(--white)}
  .stat{color:var(--white);font-size:10.5px;line-height:12px}
  .stat b{font-size:12.5px;font-weight:500;display:block;margin-bottom:4px}
  .stat .muted{color:rgba(255,255,255,.7)}
  .divider-v{left:141px;top:399px;width:1px;height:72px;background:rgba(255,255,255,.8)}
  .divider-h{left:10px;right:4px;top:482px;height:1px;background:rgba(255,255,255,.8)}
  .chart{left:106px;top:498px;width:168px;height:70px}
</style>
</head>
<body>
<main class="canvas">

  <!-- Splash -->
  <section class="screen splash" aria-label="Welcome screen">
    <div class="abs brand">Brisko Routine</div>
    <div class="abs btn-outline" style="top:205px">Login</div>
    <div class="abs btn-outline" style="top:257px">Signup</div>
  </section>

  <!-- Home list -->
  <section class="screen phone home" aria-label="Workout list">
    <div class="abs home-header"></div>
    <div class="abs status"><span>9:41</span><svg viewBox="0 0 48 10"><g fill="#fff"><rect x="0" y="6" width="2.5" height="4"/><rect x="4" y="4" width="2.5" height="6"/><rect x="8" y="2" width="2.5" height="8"/><rect x="12" y="0" width="2.5" height="10"/><path d="M20 3.5a9 9 0 0 1 12 0l-1.3 1.4a7 7 0 0 0-9.4 0zM22.6 6.2a5 5 0 0 1 6.8 0L26 9.6z"/><rect x="34" y="1" width="14" height="8" rx="2"/></g></svg></div>
    <svg class="abs burger" viewBox="0 0 24 20"><g stroke="#fff" stroke-width="1.6"><line x1="0" y1="2" x2="24" y2="2"/><line x1="0" y1="10" x2="24" y2="10"/><line x1="0" y1="18" x2="24" y2="18"/></g></svg>
    <div class="abs brand">Brisko Routine</div>
    <div class="abs tabs" style="top:82px"><div class="tab active">Popular Workouts</div><div class="tab">Trending Workouts</div></div>
    <div class="abs card photo-gym" style="top:121px" role="img" aria-label="Group doing lunges in a gym"><span class="card-caption">Touch Your Toes (Flexibility Hack)</span></div>
    <div class="abs card photo-push" style="top:245px" role="img" aria-label="Man doing push-ups"><span class="card-caption">Touch Your Toes (Flexibility Hack)</span></div>
    <div class="abs card photo-ball" style="top:370px" role="img" aria-label="Woman stretching on an exercise ball"><span class="card-caption">Touch Your Toes (Flexibility Hack)</span></div>
    <div class="abs card photo-ball" style="top:495px;height:63px" role="img" aria-label="Woman stretching on an exercise ball"></div>
    <nav class="abs navbar">
      <div class="nav-item"><svg viewBox="0 0 20 20"><path d="M5 2c2 0 3 2 3 5s-1 5-3 5-3-2-3-5 1-5 3-5zM3.5 14h3v2a1.5 1.5 0 0 1-3 0zM14 4c2 0 3 2 3 5s-1 5-3 5-3-2-3-5 1-5 3-5zM12.5 16h3v1.5a1.5 1.5 0 0 1-3 0z"/></svg>Steps</div>
      <div class="nav-item active"><svg viewBox="0 0 20 20"><path d="M2 9 10 2l8 7v9H2zM8 18v-5h4v5"/></svg>Home</div>
      <div class="nav-item"><svg viewBox="0 0 20 20"><circle cx="10" cy="8" r="6"/><path d="M10 5l1 2 2 .3-1.5 1.4.4 2.1L10 9.8l-1.9 1 .4-2.1L7 7.3 9 7zM6 13l-2 5 3-1 1.5 2 1.5-4.5M14 13l2 5-3-1-1.5 2L10 14.5"/></svg>Challenges</div>
    </nav>
  </section>

  <!-- Workout detail -->
  <section class="screen phone detail" aria-label="Workout video screen">
    <div class="abs video photo-gym" role="img" aria-label="Workout video of a group doing lunges"></div>
    <div class="abs status"><span>9:41</span><svg viewBox="0 0 48 10"><g fill="#fff"><rect x="0" y="6" width="2.5" height="4"/><rect x="4" y="4" width="2.5" height="6"/><rect x="8" y="2" width="2.5" height="8"/><rect x="12" y="0" width="2.5" height="10"/><path d="M20 3.5a9 9 0 0 1 12 0l-1.3 1.4a7 7 0 0 0-9.4 0zM22.6 6.2a5 5 0 0 1 6.8 0L26 9.6z"/><rect x="34" y="1" width="14" height="8" rx="2"/></g></svg></div>
    <div class="abs progress"><span>02:23</span><div class="track"><div class="knob"></div></div><span>08:00</span></div>
    <div class="abs label-small">Title</div>
    <h2 class="abs detail-title">Touch Your Toes (Flexibility Hack)</h2>
    <p class="abs detail-desc">Here's a very quick secret to touching your toes! It'll get you<br>way more flexible in under a minute to finally reach the ground.<br>Aim low, dream high.</p>
    <div class="abs tabs"><div class="tab active">Comments</div><div class="tab">F.A.Q</div></div>
    <div class="abs comment" style="top:335px">
      <div class="avatar"></div>
      <div><div class="comment-name">Jonah Merrit</div>
        <div class="comment-text">This app is so good for those people who<br>cannot have time for gym</div>
        <div class="comment-meta"><span><svg width="10" height="9" viewBox="0 0 10 9"><path d="M5 9 1 5A2.3 2.3 0 0 1 5 1.6 2.3 2.3 0 0 1 9 5z" fill="#8a8f94"/></svg>543</span>Reply</div></div>
    </div>
    <div class="abs comment-divider" style="top:406px"></div>
    <div class="abs comment" style="top:420px">
      <div class="avatar"></div>
      <div><div class="comment-name">Alden Cole</div>
        <div class="comment-text" style="margin-top:8px">Full body workouts, legs, arms and shoulders;<br>Anything and everything. No equipment<br>needed.</div>
        <div class="comment-meta" style="margin-top:6px"><span><svg width="10" height="9" viewBox="0 0 10 9"><path d="M5 9 1 5A2.3 2.3 0 0 1 5 1.6 2.3 2.3 0 0 1 9 5z" fill="#e0211f"/></svg>231</span>Reply</div></div>
    </div>
    <div class="abs comment-input">Write your comment here...<svg width="26" height="16" viewBox="0 0 26 16"><path d="M1 8 25 1 19 15 12 10zM12 10l13-9" fill="none" stroke="#8a8f94" stroke-width="1.3"/></svg></div>
    <nav class="abs navbar">
      <div class="nav-item"><svg viewBox="0 0 20 20"><path d="M5 2c2 0 3 2 3 5s-1 5-3 5-3-2-3-5 1-5 3-5zM3.5 14h3v2a1.5 1.5 0 0 1-3 0zM14 4c2 0 3 2 3 5s-1 5-3 5-3-2-3-5 1-5 3-5zM12.5 16h3v1.5a1.5 1.5 0 0 1-3 0z"/></svg>Steps</div>
      <div class="nav-item"><svg viewBox="0 0 20 20"><path d="M2 9 10 2l8 7v9H2zM8 18v-5h4v5"/></svg>Home</div>
      <div class="nav-item"><svg viewBox="0 0 20 20"><circle cx="10" cy="8" r="6"/><path d="M10 5l1 2 2 .3-1.5 1.4.4 2.1L10 9.8l-1.9 1 .4-2.1L7 7.3 9 7zM6 13l-2 5 3-1 1.5 2 1.5-4.5M14 13l2 5-3-1-1.5 2L10 14.5"/></svg>Challenges</div>
    </nav>
  </section>

  <!-- Steps tracker -->
  <section class="screen phone steps" aria-label="Step tracker">
    <div class="abs status"><span>9:41</span><svg viewBox="0 0 48 10"><g fill="#fff"><rect x="0" y="6" width="2.5" height="4"/><rect x="4" y="4" width="2.5" height="6"/><rect x="8" y="2" width="2.5" height="8"/><rect x="12" y="0" width="2.5" height="10"/><path d="M20 3.5a9 9 0 0 1 12 0l-1.3 1.4a7 7 0 0 0-9.4 0zM22.6 6.2a5 5 0 0 1 6.8 0L26 9.6z"/><rect x="34" y="1" width="14" height="8" rx="2"/></g></svg></div>
    <svg class="abs ring" viewBox="0 0 212 212">
      <circle cx="106" cy="106" r="104" fill="none" stroke="rgba(255,255,255,.35)" stroke-width="2.5"/>
      <path d="M106 2A104 104 0 1 1 3 94" fill="none" stroke="#fff" stroke-width="2.5"/>
      <g fill="#fff">
        <path d="M82 30c10-2 16 10 15 24s-4 20-12 20-10-8-11-20 0-22 8-24zM78 80h16l-1 8c-1 7-13 7-14 0z"/>
        <path d="M130 48c-9-2-15 9-14 22s3 18 10 18 10-7 11-18 1-20-7-22zM116 94h15l-1 8c-1 7-12 7-13 0z"/>
      </g>
    </svg>
    <div class="abs step-count">1325</div>
    <div class="abs step-label">Steps</div>

    <svg class="abs" style="left:34px;top:418px" width="34" height="30" viewBox="0 0 34 30"><g fill="none" stroke="#fff" stroke-width="2"><path d="M29 2a4 4 0 0 1 4 4c0 3-4 7-4 7s-4-4-4-7a4 4 0 0 1 4-4zM6 18a4 4 0 0 1 4 4c0 3-4 7-4 7s-4-4-4-7a4 4 0 0 1 4-4zM26 14H14M30 19H14M30 24H14"/></g></svg>
    <div class="abs stat" style="left:83px;top:413px">Distance<b>2.03km</b><span class="muted">Goal</span><b>8km</b></div>
    <div class="abs divider-v"></div>
    <svg class="abs" style="left:171px;top:418px" width="22" height="32" viewBox="0 0 22 32"><path d="M11 1c2 7 10 11 10 20a10 10 0 0 1-20 0c0-5 3-8 5-10 0 4 2 6 3 6 0-6 0-11 2-16zM11 20c3 3 4 5 4 7a4 4 0 0 1-8 0c0-2 2-4 4-7z" fill="#fff" fill-rule="evenodd"/></svg>
    <div class="abs stat" style="left:212px;top:413px">Calories<b>680</b><span class="muted">Goal</span><b>4,850</b></div>
    <div class="abs divider-h"></div>

    <svg class="abs" style="left:16px;top:520px" width="26" height="26" viewBox="0 0 26 26"><path d="M14 1A12 12 0 1 0 25 17 10 10 0 0 1 14 1z" fill="#fff"/></svg>
    <div class="abs stat" style="left:62px;top:508px">Sleep<b>7h35</b><span class="muted">Goal</span><b>8h00</b></div>
    <svg class="abs chart" viewBox="0 0 168 70">
      <defs><linearGradient id="sleepFill" x1="0" y1="0" x2="1" y2="0"><stop offset="0" stop-color="#35d6b8"/><stop offset="1" stop-color="#35b8e0"/></linearGradient></defs>
      <path d="M4 70V40C10 26 22 24 36 27S56 33 66 33 80 28 94 33 116 36 124 32 146 30 166 26V70z" fill="url(#sleepFill)" opacity=".95"/>
      <text x="24" y="19" fill="#fff" font-size="9" font-family="Roboto, sans-serif">8h00</text>
      <text x="62" y="27" fill="#fff" font-size="9" font-family="Roboto, sans-serif">7h30</text>
      <text x="100" y="29" fill="#fff" font-size="9" font-family="Roboto, sans-serif">7h28</text>
      <text x="138" y="24" fill="#fff" font-size="9" font-family="Roboto, sans-serif">7h35</text>
    </svg>
    <nav class="abs navbar" style="height:42px">
      <div class="nav-item active"><svg viewBox="0 0 20 20"><path d="M5 2c2 0 3 2 3 5s-1 5-3 5-3-2-3-5 1-5 3-5zM3.5 14h3v2a1.5 1.5 0 0 1-3 0zM14 4c2 0 3 2 3 5s-1 5-3 5-3-2-3-5 1-5 3-5zM12.5 16h3v1.5a1.5 1.5 0 0 1-3 0z"/></svg>Steps</div>
      <div class="nav-item"><svg viewBox="0 0 20 20"><path d="M2 9 10 2l8 7v9H2zM8 18v-5h4v5"/></svg>Home</div>
      <div class="nav-item"><svg viewBox="0 0 20 20"><circle cx="10" cy="8" r="6"/><path d="M10 5l1 2 2 .3-1.5 1.4.4 2.1L10 9.8l-1.9 1 .4-2.1L7 7.3 9 7zM6 13l-2 5 3-1 1.5 2 1.5-4.5M14 13l2 5-3-1-1.5 2L10 14.5"/></svg>Challenges</div>
    </nav>
  </section>

</main>
</body>
</html>
```